Custom unique Stationary design for Logistics company

We need a custom, unique , elegant and luxurious full stationary design using our new logo, following these guidelines:
1- Business card: double sided, both sides uses the navy blue as the background main color (same as the code of the navy blue used in our logo).
2- envelope and folder: also use the same navy blue as the main background color.
3- book cover( notepad cover) : same thing with the navy blue
4- letterhead: feel free to use the combination of the colors in our logo.
5- rest of the items are up to your creativity

Target Market(s)

corporates and other businesses

Industry/Entity Type

Logistics and heavy machines contractors

Requirements
Must have
• Letterhead, business card, envelope, notepad cover, paper, file
Nice to have
• navy blue to be main background color for business card, envelope, notepad cover

```html
<!DOCTYPE html>
<html lang="en">
<head>
<meta charset="utf-8">
<title>Northvale Freight – Business Card</title>
<link rel="stylesheet" href="https://fonts.googleapis.com/css2?family=Exo+2:wght@400;700&display=swap">
<style>
  :root{
    --navy:#00507a;
    --orange:#f05a28;
    --white:#ffffff;
    --ink:#4a4a4a;
    --cyan:#1fe3f7;
    --backdrop:#8c8c8c;
  }
  *{margin:0;padding:0;box-sizing:border-box}
  html,body{width:1200px;height:1200px;overflow:hidden}
  body{background:var(--backdrop);font-family:"Exo 2",sans-serif;position:relative}
  .card{position:absolute;left:262px;width:685px;height:391px;border-radius:26px;overflow:hidden;background:var(--navy)}
  .card-front{top:165px}
  .card-back{top:653px}
  .card-art{position:absolute;inset:0;width:100%;height:100%}
  .brand-name{position:absolute;color:var(--white);font-weight:700;letter-spacing:1px;line-height:1.05;text-transform:uppercase}
  .card-front .brand-name{left:68px;top:88px;font-size:40px}
  .card-back .brand-name{left:0;right:0;top:150px;text-align:center;font-size:44px;color:var(--cyan)}
  .contact{position:absolute;right:33px;top:192px;text-align:right;color:var(--ink)}
  .contact .name{color:var(--orange);font-size:23px;font-weight:400;letter-spacing:.5px}
  .contact .title{font-size:14px;color:#333;margin-top:2px}
  .contact .address{font-size:14px;margin-top:9px;line-height:19px}
  .contact ul{list-style:none;margin-top:9px;font-size:14px;line-height:19.5px}
  .contact li{display:flex;justify-content:flex-end;align-items:center;gap:8px}
  .contact li svg{width:12px;height:12px;fill:var(--orange);flex:none}
</style>
</head>
<body>
  <section class="card card-front">
    <svg class="card-art" viewBox="0 0 800 457" preserveAspectRatio="none" aria-hidden="true">
      <path fill="var(--orange)" d="M612,0 C660,35 655,100 597,165 C480,295 300,400 100,457 L180,457 C330,380 500,270 600,140 C645,80 650,30 610,0Z"/>
      <path fill="var(--white)" d="M610,0 C650,30 645,80 600,140 C500,270 330,380 180,457 L800,457 L800,0Z"/>
    </svg>
    <div class="brand-name">Northvale<br>Freight</div>
    <div class="contact">
      <div class="name">DANIEL ROWE</div>
      <div class="title">President</div>
      <div class="address">412 Harbor Road<br>Juneau, Alaska 99801</div>
      <ul>
        <li>555-201-4488 <svg viewBox="0 0 24 24"><path d="M6.6 10.8a15 15 0 0 0 6.6 6.6l2.2-2.2a1 1 0 0 1 1-.25 11.4 11.4 0 0 0 3.6.6 1 1 0 0 1 1 1V20a1 1 0 0 1-1 1A17 17 0 0 1 3 4a1 1 0 0 1 1-1h3.5a1 1 0 0 1 1 1c0 1.25.2 2.45.6 3.6a1 1 0 0 1-.25 1z"/></svg></li>
        <li>555-318-7702 <svg viewBox="0 0 24 24"><path d="M7 1h10a2 2 0 0 1 2 2v18a2 2 0 0 1-2 2H7a2 2 0 0 1-2-2V3a2 2 0 0 1 2-2zm0 3v15h10V4z"/></svg></li>
        <li>info@northvalefreight.com <svg viewBox="0 0 24 24"><path d="M2 5h20v14H2z M2 5l10 8 10-8" fill="var(--orange)"/><path d="M3 6l9 7 9-7" fill="none" stroke="#fff" stroke-width="1.5"/></svg></li>
        <li>northvalefreight.com <svg viewBox="0 0 24 24"><circle cx="12" cy="12" r="10"/><path d="M12 2a15 10 0 0 0 0 20M2 12h20" fill="none" stroke="#fff" stroke-width="1.5"/></svg></li>
      </ul>
    </div>
  </section>

  <section class="card card-back">
    <div class="brand-name">Northvale Freight</div>
  </section>
</body>
</html>
```